Trifold Total Body Wellness pamphlet for dental patients

I had Chat GPT help create and layout a pamphlet to be used in my dental office. I placed the wording and would like a graphic designer to make it better so I can get it printed and start handing it out to patients. We are a science driven dental office with the goal of total body wellness. Our main colors our black, white and gray with red as an accent color. We like a modern and clean look. We are an established dental practice and would like to evolve the way we do things when science shows a better way. This pamphlet will help explain to our existing patients why we are doing things differently and how it will better help us treat the disease in their mouths.

```html
<!DOCTYPE html>
<html lang="en">
<head>
<meta charset="utf-8">
<title>Total Body Wellness</title>
<link href="https://fonts.googleapis.com/css2?family=Poppins:wght@300;400;500;600;700&display=swap" rel="stylesheet">
<style>
:root{
  --red:#d22128;
  --ink:#161616;
  --text:#2b2b2b;
  --muted:#f3f3f4;
  --rule:#dedede;
  --white:#ffffff;
}
*{margin:0;padding:0;box-sizing:border-box}
html,body{width:1200px;height:933px;overflow:hidden;background:var(--white)}
body{font-family:'Poppins',sans-serif;color:var(--text);position:relative}
.abs{position:absolute}
.title{font-weight:400;color:var(--ink);line-height:1.04;letter-spacing:.2px}
.title strong{display:block;font-weight:700;color:var(--red)}
.bar{position:absolute;height:4px;background:var(--red)}
p.body{font-size:14.6px;font-weight:300;line-height:20px;color:var(--text)}
p.body + p.body{margin-top:7px}

/* left panel */
.panel-left .title{font-size:37px;left:27px;top:28px}
.test-heading{left:30px;top:397px;font-size:21px;font-weight:500;letter-spacing:.6px;color:var(--ink)}
.test-list{left:27px;top:434px;list-style:none}
.test-list li{display:flex;align-items:center;height:59.3px}
.count{width:50px;height:50px;border-radius:50%;background:var(--red);color:#fff;font-size:25px;font-weight:400;display:flex;align-items:center;justify-content:center}
.test-name{margin-left:26px;font-size:12.6px;font-weight:400;color:var(--ink)}
.steps{left:27px;top:827px;width:364px;height:80px;background:var(--muted);border-radius:10px}
.step{position:absolute;top:0;height:80px;width:80px;text-align:center;font-size:11.2px;color:var(--ink)}
.step svg{position:absolute;top:15px;left:25px}
.step span{position:absolute;top:52px;left:0;right:0;white-space:nowrap}

/* middle panel */
.panel-mid .title,.panel-right .title{font-size:34px;line-height:36.5px}
.organ{position:absolute;width:140px}
.organ .icon{position:absolute;left:0;top:0;width:30px;height:30px;border-radius:50%;background:var(--ink);display:flex;align-items:center;justify-content:center}
.organ h3{position:absolute;left:37px;top:0;font-size:14.4px;font-weight:500;color:var(--ink);line-height:16px;letter-spacing:.2px;white-space:nowrap}
.organ p{position:absolute;left:37px;font-size:10.3px;line-height:12px;font-weight:400;color:var(--ink)}
.figure{left:520px;top:282px;width:140px;height:512px;border-radius:60px 60px 30px 30px;background:radial-gradient(ellipse at 50% 30%,#e7d6d6 0%,#efeaea 45%,#f7f6f6 80%,#fff 100%)}
.wires{left:0;top:0}

/* right panel */
.svc{position:absolute;left:813px;width:240px}
.svc .kicker{font-size:16.3px;font-weight:500;color:var(--red);letter-spacing:.6px;line-height:19px}
.svc h3{font-size:16.3px;font-weight:500;color:var(--ink);letter-spacing:.6px;line-height:20px;white-space:nowrap}
.svc p{font-size:12.9px;font-weight:300;line-height:20px;color:var(--ink);margin-top:3px}
.svc .tag{font-size:13.4px;font-weight:500;color:var(--red);margin-top:6px}
.svc ul{list-style:none;margin-top:1px}
.svc li{font-size:12.9px;font-weight:300;line-height:14.5px;color:var(--ink);padding-left:16px;position:relative;margin-bottom:7px}
.svc li::before{content:"";position:absolute;left:1px;top:6px;width:4px;height:4px;border-radius:50%;background:var(--ink)}
.photo{position:absolute}
.divider{position:absolute;left:813px;width:358px;height:1px;background:var(--rule)}

/* footer band */
.band{left:418px;top:843px;width:782px;height:90px;background:var(--ink);border-radius:16px 0 0 0}
.band .badge{position:absolute;left:24px;top:21px;width:46px;height:46px;border-radius:50%;background:var(--red);display:flex;align-items:center;justify-content:center}
.band p{position:absolute;left:81px;color:#fff;font-size:13.4px;font-weight:300;line-height:14px}
.band b{font-weight:600}
</style>
</head>
<body>

<!-- LEFT PANEL -->
<section class="panel-left">
  <h1 class="title abs">BLEEDING IS<strong>NOT NORMAL</strong></h1>
  <div class="bar" style="left:27px;top:119px;width:81px"></div>
  <div class="abs" style="left:30px;top:134px;width:365px">
    <p class="body">If your gums bleed when you brush or floss, your body is signaling that inflammation is present. Healthy gums should not bleed.</p>
    <p class="body">In many cases, bleeding is caused by harmful bacteria living below the gumline. Left untreated, these pathogens can contribute to chronic inflammation that affects not only your oral health but may also influence your overall health.</p>
    <p class="body">Rather than guessing which bacteria are present, we can identify them through advanced salivary testing.</p>
  </div>
  <div class="abs" style="left:30px;top:383px;width:357px;height:1px;background:var(--rule)"></div>
  <h2 class="test-heading abs">WHAT WE TEST FOR</h2>
  <ul class="test-list abs">
    <li><span class="count">30</span><span class="test-name">PERIODONTAL PATHOGENS</span></li>
    <li><span class="count">12</span><span class="test-name">CARIES PATHOGENS</span></li>
    <li><span class="count">10</span><span class="test-name">CANDIDA SPECIES</span></li>
    <li><span class="count">7</span><span class="test-name">HERPES VIRUSES</span></li>
  </ul>
  <p class="body abs" style="left:27px;top:679px;width:370px;font-size:15.4px">This comprehensive analysis allows us to create an individualized whole-mouth disinfection protocol designed specifically for your microbiome.</p>
  <div class="bar" style="left:27px;top:764px;width:59px;height:3px"></div>
  <p class="body abs" style="left:27px;top:778px;width:370px;font-size:15.4px">Instead of treating every patient the same, we treat your unique biology.</p>
  <div class="steps abs">
    <div class="step" style="left:0">
      <svg width="30" height="30" viewBox="0 0 30 30" fill="none" stroke="#d22128" stroke-width="2"><circle cx="15" cy="15" r="8"/><path d="M15 2v5M15 23v5M2 15h5M23 15h5M6 6l3.5 3.5M20.5 20.5L24 24M24 6l-3.5 3.5M9.5 20.5L6 24"/><circle cx="13" cy="13" r="1.3" fill="#d22128"/><circle cx="17.5" cy="16.5" r="1.3" fill="#d22128"/></svg>
      <span>MEASURE</span>
    </div>
    <div class="step" style="left:101px">
      <svg width="30" height="30" viewBox="0 0 30 30" fill="none" stroke="#d22128" stroke-width="2.2"><circle cx="15" cy="15" r="13"/><circle cx="15" cy="12" r="4.5"/><path d="M7 24c2-4 5-5.5 8-5.5s6 1.5 8 5.5"/></svg>
      <span>PERSONALIZE</span>
    </div>
    <div class="step" style="left:201px"><span>TREAT</span></div>
    <div class="step" style="left:278px">
      <svg width="30" height="30" viewBox="0 0 30 30" fill="none" stroke="#d22128" stroke-width="2.2"><path d="M5 12a10.5 10.5 0 0 1 18-4.5"/><path d="M24 3v5h-5"/><path d="M25 18a10.5 10.5 0 0 1-18 4.5"/><path d="M6 27v-5h5"/></svg>
      <span>RETEST</span>
    </div>
  </div>
</section>

<!-- MIDDLE PANEL -->
<section class="panel-mid">
  <h1 class="title abs" style="left:418px;top:26px">BEYOND THE MOUTH<strong>THE ORAL-SYSTEMIC</strong><strong>CONNECTION</strong></h1>
  <div class="bar" style="left:418px;top:144px;width:81px"></div>
  <div class="abs" style="left:419px;top:162px;width:375px">
    <p class="body" style="font-size:15px;line-height:21px">Inflammation caused by harmful oral pathogens doesn't stay in your mouth.</p>
    <p class="body" style="font-size:15px;line-height:21px">These bacteria, fungi, and viruses can enter the bloodstream and affect your entire body</p>
  </div>

  <div class="figure abs" role="img" aria-label="Anatomical human figure showing the circulatory system with the heart highlighted in red"></div>

  <svg class="wires abs" width="1200" height="933" viewBox="0 0 1200 933" fill="none" stroke="#d22128" stroke-width="0.8">
    <path d="M509 291H583"/>
    <path d="M686 302V416H613"/>
    <path d="M520 461H533"/>
    <path d="M624 485H672"/>
    <path d="M543 657V547H590"/>
    <path d="M624 678H672"/>
  </svg>

  <div class="organ" style="left:419px;top:278px">
    <span class="icon"><svg width="18" height="18" viewBox="0 0 18 18" fill="none" stroke="#fff" stroke-width="1.5"><path d="M5 16v-3.5C3 11.5 2 9.5 2.5 7 3.3 3.5 6.5 2 9.5 2.3c3.5.4 5.7 3.3 5 6.5l1 2.5h-1.5V14h-3v2"/><circle cx="9" cy="7.5" r="1.6"/></svg></span>
    <h3>BRAIN</h3>
    <p style="top:20px">Linked to<br>cognitive<br>decline,<br>Alzheimer's<br>disease and<br>stroke risk.</p>
  </div>
  <div class="organ" style="left:673px;top:283px">
    <span class="icon"><svg width="18" height="18" viewBox="0 0 18 18" fill="none" stroke="#fff" stroke-width="1.6"><path d="M9 15.5S2 11 2 6.3A3.5 3.5 0 0 1 9 5a3.5 3.5 0 0 1 7 1.3C16 11 9 15.5 9 15.5z"/></svg></span>
    <h3>HEART</h3>
    <p style="top:20px">Associated<br>with increased<br>risk of heart<br>disease,<br>inflammation<br>and high<br>blood<br>pressure.</p>
  </div>
  <div class="organ" style="left:419px;top:453px">
    <span class="icon"><svg width="18" height="18" viewBox="0 0 18 18" fill="none" stroke="#fff" stroke-width="1.4"><path d="M9 2v7M9 8l-2 2M9 8l2 2"/><path d="M6.5 6C4 6 2 10 2 14c0 1.5 1 2 2.5 1.5L7 14V8.5"/><path d="M11.5 6C14 6 16 10 16 14c0 1.5-1 2-2.5 1.5L11 14V8.5"/></svg></span>
    <h3>LUNGS</h3>
    <p style="top:20px">Linked to<br>respiratory<br>infections,<br>COPD and<br>worsening<br>lung<br>conditions.</p>
  </div>
  <div class="organ" style="left:673px;top:470px">
    <span class="icon"><svg width="18" height="18" viewBox="0 0 18 18" fill="none" stroke="#fff" stroke-width="1.6"><path d="M9 2C9 2 3.5 8.5 3.5 11.5a5.5 5.5 0 0 0 11 0C14.5 8.5 9 2 9 2z"/></svg></span>
    <h3>BLOOD<br>SUGAR</h3>
    <p style="top:37px">Associated<br>with insulin<br>resistance and<br>poor diabetes<br>control.</p>
  </div>
  <div class="organ" style="left:419px;top:663px">
    <span class="icon"><svg width="18" height="18" viewBox="0 0 18 18" fill="none" stroke="#fff" stroke-width="1.4"><circle cx="9" cy="9" r="7.5"/><circle cx="9" cy="5.5" r="1.5"/><path d="M7.5 8.5h3c1.5 0 2 1.5 2 2.5s-1 2-2.5 2H7.5z"/></svg></span>
    <h3>PREGNANCY</h3>
    <p style="top:20px">Linked to<br>preterm birth,<br>low birth<br>weight and<br>preeclampsia.</p>
  </div>
  <div class="organ" style="left:673px;top:663px">
    <span class="icon"><svg width="18" height="18" viewBox="0 0 18 18" fill="none" stroke="#fff" stroke-width="1.5"><path d="M5 2c0 5 8 6 8 11M13 2c0 2-1 3-3 4.2M8 11.8C6 13 5 14 5 16"/><path d="M6 4.5h6M6 13.5h6"/></svg></span>
    <h3>JOINTS &amp;<br>IMMUNITY</h3>
    <p style="top:39px">May contribute<br>to arthritis,<br>autoimmune<br>flares and a<br>weakened<br>immune<br>response.</p>
  </div>
</section>

<!-- RIGHT PANEL -->
<section class="panel-right">
  <h1 class="title abs" style="left:812px;top:26px">ADVANCED WELLNESS<strong>SCREENING IN OUR</strong><strong>OFFICE</strong></h1>
  <div class="bar" style="left:812px;top:144px;width:81px"></div>

  <div class="svc" style="top:176px;width:245px">
    <div class="kicker">LUMASCAN</div>
    <h3>ORAL CANCER SCREENNG</h3>
    <p>Advanced fluorescence technology helps detect absormal cells early, when treatment is most effective.</p>
    <div class="tag">Early detection saves lives.</div>
  </div>
  <div class="photo" role="img" aria-label="Oral cancer screening device: black tablet screen on a white stand" style="left:1066px;top:150px;width:104px;height:180px;background:linear-gradient(180deg,#1a1a1a 0%,#1a1a1a 58%,#e9e9ea 62%,#f6f6f6 100%);border-radius:4px"></div>

  <div class="divider" style="top:336px"></div>

  <div class="svc" style="top:373px;width:240px">
    <div class="kicker">COMPLIMENTARY</div>
    <h3>HOME SLEEP SCREENING</h3>
    <p style="margin-bottom:5px">We have two home overnight oxygen monitors available for you to check out at no charge.</p>
    <ul>
      <li>Wear the monitor for 2-3 nights</li>
      <li>Painless and easy to use</li>
      <li style="width:225px">We provide a detailed report for you to take to your physician if further evaluation is needed</li>
    </ul>
    <div class="tag" style="margin-top:8px">Better sleep. Better health.</div>
  </div>
  <div class="photo" role="img" aria-label="Black wrist oxygen monitor with a white finger sensor" style="left:1060px;top:412px;width:113px;height:175px;background:radial-gradient(ellipse at 55% 40%,#1c1c1c 0%,#2a2a2a 45%,#e8e8e8 70%,#fff 100%)"></div>

  <div class="divider" style="top:627px"></div>

  <div class="svc" style="top:660px;width:240px">
    <div class="kicker">APOE GENETIC</div>
    <h3>WELLNESS TESTING</h3>
    <p>Understand your inherited genetic variant associated with increased Alzheimer's disease risk so you can take a more personalized approach to your long-term brain health.</p>
  </div>
  <div class="photo" role="img" aria-label="White DNA double helix" style="left:1060px;top:632px;width:110px;height:210px;background:linear-gradient(160deg,#fafafa 0%,#e6e6e6 50%,#f7f7f7 100%);border-radius:40px"></div>
</section>

<!-- FOOTER BAND -->
<footer class="band abs">
  <span class="badge"><svg width="22" height="24" viewBox="0 0 22 24" fill="#fff"><path d="M11 4C8 1.5 2 1.5 1.5 7c-.3 3.5 1.5 5.5 2.5 9 .8 3 1 7 3 7s2-5 4-5 2 5 4 5 2.2-4 3-7c1-3.5 2.8-5.5 2.5-9C20 1.5 14 1.5 11 4z"/></svg></span>
  <p style="top:20px">Chronic oral inflammation is linked to more than <b>70 systemic diseases.</b></p>
  <p style="top:42px;width:680px">Your oral health is connected to your total body health. We never stop learning so you can keep living a healthier, longer life.</p>
</footer>

</body>
</html>
```